Business Card Designs

Looking to design a 3.5" x 2" standard business card for our employees.
The design needs to be sleek, simple, and modern. We would like our logo (attached) to be incorporated, but not in that colour, rather an outline of the logo in either gold or silver (whichever looks better).

Modern and Simple is what we are looking for, but be creative in incorporating the logo.

```html
<!DOCTYPE html>
<html lang="en">
<head>
<meta charset="utf-8">
<title>Harbourline Suites – Business Card</title>
<link href="https://fonts.googleapis.com/css2?family=Open+Sans:wght@400;600;700&display=swap" rel="stylesheet">
<style>
  :root {
    --backdrop: #d6d6d6;
    --paper: #eeeeec;
    --teal: #4f9796;
    --ink: #5a5a5a;
    --white: #ffffff;
  }
  * { margin: 0; padding: 0; box-sizing: border-box; }
  html, body { width: 1200px; height: 1051px; overflow: hidden; }
  body {
    background: var(--backdrop);
    font-family: "Open Sans", Arial, sans-serif;
    display: flex;
    align-items: center;
    justify-content: center;
    gap: 44px;
  }
  .card {
    width: 525px;
    height: 300px;
    position: relative;
    box-shadow: 0 6px 18px rgba(0,0,0,0.12);
  }
  .card--front { background: var(--paper); }
  .card--back {
    background: var(--teal);
    display: flex;
    align-items: center;
    justify-content: center;
  }
  .person {
    position: absolute;
    left: 58px;
    top: 92px;
    width: 190px;
    text-align: right;
  }
  .person__name {
    color: var(--teal);
    font-weight: 700;
    font-size: 19px;
    letter-spacing: 0.5px;
    text-transform: uppercase;
    white-space: nowrap;
  }
  .person__role {
    color: var(--ink);
    font-size: 13px;
    margin-top: 2px;
  }
  .divider {
    position: absolute;
    left: 268px;
    top: 112px;
    width: 2px;
    height: 66px;
    background: var(--teal);
  }
  .contact {
    position: absolute;
    left: 288px;
    top: 116px;
    list-style: none;
    color: var(--ink);
    font-size: 13px;
    line-height: 20px;
  }
  .contact__item { display: flex; align-items: center; gap: 7px; white-space: nowrap; }
  .contact__icon { width: 11px; height: 11px; fill: var(--teal); flex: none; }
  .address {
    position: absolute;
    left: 0;
    right: 0;
    bottom: 52px;
    text-align: center;
    color: var(--ink);
    font-size: 13px;
  }
  .brand {
    display: flex;
    align-items: center;
    gap: 12px;
    color: var(--white);
    font-weight: 600;
    font-size: 22px;
    letter-spacing: 3px;
    text-transform: uppercase;
  }
  .brand__mark {
    width: 16px;
    height: 16px;
    background: var(--white);
  }
</style>
</head>
<body>
  <section class="card card--front">
    <div class="person">
      <p class="person__name">Arlen Marchetti</p>
      <p class="person__role">President</p>
    </div>
    <div class="divider"></div>
    <ul class="contact">
      <li class="contact__item">
        <svg class="contact__icon" viewBox="0 0 24 24" aria-hidden="true"><path d="M6.6 10.8a15.1 15.1 0 0 0 6.6 6.6l2.2-2.2a1 1 0 0 1 1-.25 11.4 11.4 0 0 0 3.6.57 1 1 0 0 1 1 1V20a1 1 0 0 1-1 1A17 17 0 0 1 3 4a1 1 0 0 1 1-1h3.5a1 1 0 0 1 1 1c0 1.25.2 2.45.57 3.57a1 1 0 0 1-.25 1z"/></svg>
        555-014-2286
      </li>
      <li class="contact__item">
        <svg class="contact__icon" viewBox="0 0 24 24" aria-hidden="true"><path d="M2 5h20v14H2z M2 5l10 8 10-8" stroke="#eeeeec" stroke-width="1.5"/></svg>
        info@harbourlinesuites.com
      </li>
      <li class="contact__item">
        <svg class="contact__icon" viewBox="0 0 24 24" aria-hidden="true"><circle cx="12" cy="12" r="11"/><path d="M1 12h22M12 1c4 4 4 18 0 22M12 1c-4 4-4 18 0 22" fill="none" stroke="#eeeeec" stroke-width="1.5"/></svg>
        www.harbourlinesuites.com
      </li>
    </ul>
    <p class="address">1480 Seabright Lane, Cove Harbor CA 90000</p>
  </section>

  <section class="card card--back">
    <div class="brand">
      <span class="brand__mark"></span>
      <span class="brand__name">Harbourline Suites</span>
    </div>
  </section>
</body>
</html>
```